professional business card design

Business card design. Photos have been uploaded and i am open to the designer choosing which photos to use. Would like the card to be mostyly in a grey scale design with black, whites, silver & grey colours. I have added copy of our flyer as would like on the back side of card our services to be listed. Do not use any bright colurs such as blue red green or yellow. i need to be able to edit the phone number and naem in the final card design submitted.

Target Market(s)

Clients

Industry/Entity Type

earhmovibng and transport

Contact Information for Business Card

Director Name, address, email, phone number and services

Colors

Designer to choose only greyscale colors for use in the design.

Requirements
Should not have
• no yellow, red, blue or green

```html
<!DOCTYPE html>
<html lang="en">
<head>
<meta charset="utf-8">
<title>KHT Pty Ltd – Business Card</title>
<link href="https://fonts.googleapis.com/css2?family=Oswald:wght@500;600&family=Montserrat:wght@400;500;600&display=swap" rel="stylesheet">
<style>
  :root {
    --page: #d9d9d9;
    --black: #0b0b0b;
    --charcoal: #1e1e1e;
    --graphite: #3a3a3a;
    --silver-light: #f2f2f2;
    --silver: #c9c9c9;
    --silver-dark: #9a9a9a;
    --white: #ffffff;
    --ink: #141414;
  }
  * { box-sizing: border-box; margin: 0; padding: 0; }
  html, body { width: 1200px; height: 1200px; overflow: hidden; }
  body {
    background: var(--page);
    display: flex;
    flex-direction: column;
    align-items: center;
    justify-content: center;
    gap: 44px;
  }
  .card {
    position: relative;
    width: 900px;
    height: 514px;
    border-radius: 34px;
    overflow: hidden;
    box-shadow: 0 10px 28px rgba(0,0,0,.28);
  }

  /* ---------- back: services ---------- */
  .card--back { background: linear-gradient(120deg, var(--silver-dark) 0%, var(--silver-light) 45%, var(--silver) 100%); }
  .services-panel {
    position: absolute; inset: 0 0 auto 0; height: 300px;
    background: radial-gradient(ellipse at 40% 30%, var(--graphite) 0%, var(--charcoal) 45%, var(--black) 100%);
    padding: 38px 60px 0;
  }
  .services-title {
    font-family: 'Oswald', sans-serif; font-weight: 600;
    color: var(--white); font-size: 34px; letter-spacing: 1px;
    text-align: left; margin-left: 190px; margin-bottom: 14px;
  }
  .services-columns { display: flex; gap: 70px; }
  .services-list { list-style: none; }
  .services-list li {
    font-family: 'Oswald', sans-serif; font-weight: 500;
    color: var(--white); font-size: 21px; line-height: 1.28;
    text-transform: uppercase; letter-spacing: .4px;
  }
  .services-list li::before { content: "• "; }
  .services-list .continued { padding-left: 14px; }
  .services-list .continued::before { content: ""; }

  .identity {
    position: absolute; left: 60px; bottom: 60px;
    border-left: 4px solid var(--ink); padding-left: 16px;
    font-family: 'Montserrat', sans-serif; color: var(--ink);
  }
  .identity-name { font-size: 44px; font-weight: 600; line-height: 1; letter-spacing: 1px; }
  .identity-role { font-size: 22px; font-weight: 400; margin-top: 6px; letter-spacing: 1px; }

  .contact {
    position: absolute; right: 56px; top: 326px; width: 420px;
    list-style: none;
    font-family: 'Montserrat', sans-serif; font-weight: 500; color: var(--ink);
    font-size: 19px; line-height: 1.3;
  }
  .contact li { display: flex; align-items: flex-start; gap: 12px; margin-bottom: 4px; }
  .contact svg { width: 20px; height: 20px; flex: none; margin-top: 2px; fill: var(--ink); }

  /* ---------- front: brand ---------- */
  .card--front { background: radial-gradient(ellipse at 45% 25%, var(--graphite) 0%, var(--charcoal) 40%, var(--black) 85%); }
  .brand {
    position: absolute; left: 200px; top: 60px;
    font-family: 'Montserrat', sans-serif; font-weight: 600; color: var(--silver);
    line-height: 1;
  }
  .brand-mark { font-size: 150px; letter-spacing: 4px; }
  .brand-suffix { font-size: 34px; margin-top: 6px; margin-left: 330px; }
  .fleet-photo {
    position: absolute; left: 230px; right: 20px; bottom: 0; height: 300px;
    background:
      radial-gradient(ellipse at 70% 40%, rgba(220,220,220,.55) 0%, rgba(120,120,120,.25) 40%, transparent 70%),
      radial-gradient(ellipse at 25% 70%, rgba(160,160,160,.45) 0%, transparent 60%),
      linear-gradient(180deg, rgba(60,60,60,.2) 0%, rgba(90,90,90,.5) 100%);
  }
</style>
</head>
<body>

<section class="card card--back">
  <div class="services-panel">
    <h2 class="services-title">Our Services</h2>
    <div class="services-columns">
      <ul class="services-list">
        <li>Over size loads / hot shot loads</li>
        <li>Heavy vehicle recovery services</li>
        <li>Potable water deliveries</li>
        <li>Road building / maintenance</li>
        <li>Earthworks</li>
        <li>Sand &amp; metal supply &amp; cartage</li>
      </ul>
      <ul class="services-list">
        <li>Road train tippers</li>
        <li>Road train tankers</li>
        <li>Road train flat tops</li>
        <li>Drop deck trailers</li>
        <li>Mine site accredited</li>
        <li class="continued">equipment &amp; operators</li>
      </ul>
    </div>
  </div>

  <div class="identity">
    <p class="identity-name">JOHN DOE</p>
    <p class="identity-role">CEO | FOUNDER</p>
  </div>

  <ul class="contact">
    <li>
      <svg viewBox="0 0 24 24" aria-hidden="true"><path d="M6.6 10.8a15 15 0 0 0 6.6 6.6l2.2-2.2a1 1 0 0 1 1-.25 11.4 11.4 0 0 0 3.6.57 1 1 0 0 1 1 1V20a1 1 0 0 1-1 1A17 17 0 0 1 3 4a1 1 0 0 1 1-1h3.5a1 1 0 0 1 1 1c0 1.25.2 2.45.57 3.57a1 1 0 0 1-.25 1z"/></svg>
      <span>(000) 000 0000</span>
    </li>
    <li>
      <svg viewBox="0 0 24 24" aria-hidden="true"><path d="M2 5h20v14H2z M2 5l10 8 10-8" fill="none" stroke="#141414" stroke-width="2"/></svg>
      <span>email@youremail.com</span>
    </li>
    <li>
      <svg viewBox="0 0 24 24" aria-hidden="true"><g fill="none" stroke="#141414" stroke-width="1.8"><circle cx="12" cy="12" r="9.5"/><ellipse cx="12" cy="12" rx="4.2" ry="9.5"/><path d="M2.5 12h19M4 7h16M4 17h16"/></g></svg>
      <span>www.yourwebsite.com</span>
    </li>
    <li>
      <svg viewBox="0 0 24 24" aria-hidden="true"><path d="M12 2a7 7 0 0 0-7 7c0 5 7 13 7 13s7-8 7-13a7 7 0 0 0-7-7zm0 9.5A2.5 2.5 0 1 1 12 6.5a2.5 2.5 0 0 1 0 5z"/></svg>
      <span>KHT Pty Ltd | Depot: Lot 14,<br>Ironbark Track Red Hill</span>
    </li>
  </ul>
</section>

<section class="card card--front">
  <div class="fleet-photo" role="img" aria-label="Black and white photograph of road train trucks lined up"></div>
  <div class="brand">
    <p class="brand-mark">KHT</p>
    <p class="brand-suffix">Pty Ltd</p>
  </div>
</section>

</body>
</html>
```